"Breakthrough! Mapping the Coastal Escape" NEEDS BOOK COVER!

Hello - please see the attached BOOK COVER DESIGN BRIEF document for full instructions and content required for cover.

I am really seeking clean, professional designs here that follow my instructions. The cover MUST jump out in a thumbnail (as if on Brindlow) - any covers that are too busy, messy or unprofessional will be eliminated.

Any questions please ask.

Thanks.
Colin
Updates

Project Deadline Extended
Reason: This project has been extended to invite more designers, as I haven't received enough options to choose from. Hoping this extra few days allows a few more submissions. Thank you to existing designers for your submissions, a number of them are in the running.

Target Market(s)

Please see the attached brief for full instructions on this project.

Industry/Entity Type

Property

Font styles to use
Serif
Sans Serif

Requirements
Must have
• Please see the attached brief for full instructions on this project.
Nice to have
Should not have

```html
<!DOCTYPE html>
<html lang="en">
<head>
<meta charset="utf-8">
<title>Breakthrough! Mapping the Coastal Escape – Book Cover</title>
<link href="https://fonts.googleapis.com/css2?family=Arimo:ital,wght@0,400;1,400&family=Open+Sans:wght@300;400;600&family=Oswald:wght@700&display=swap" rel="stylesheet">
<style>
  :root {
    --sky-light: #5fb0e6;
    --sky-mid: #3d93d6;
    --sky-deep: #2a7cc4;
    --band-blue: #1f6fb8;
    --navy: #0f2a4a;
    --stamp-red: #d62a2a;
    --white: #ffffff;
    --text-dark: #14263d;
    --house-top: #eef3f7;
    --house-photo-wall: #e9eef2;
    --photo-tone: #d9c2b0;
  }
  * { box-sizing: border-box; margin: 0; padding: 0; }
  html, body { width: 1200px; height: 841px; overflow: hidden; background: var(--white); }
  .spread {
    position: relative; width: 1200px; height: 841px; overflow: hidden;
    font-family: "Open Sans", Arial, sans-serif; color: var(--text-dark);
  }

  /* Back cover */
  .back-cover {
    position: absolute; left: 0; top: 0; width: 582px; height: 756px;
    background: linear-gradient(180deg, var(--sky-light) 0%, var(--sky-mid) 60%, var(--sky-deep) 100%);
  }
  .back-copy {
    position: absolute; left: 30px; top: 10px; width: 548px;
    font-family: "Arimo", Arial, sans-serif; font-size: 11.6px; line-height: 14.6px;
    text-align: justify;
  }
  .back-copy p { margin-bottom: 9px; }
  .back-copy ul { margin: 0 0 9px 16px; text-align: left; }
  .back-copy li { margin-bottom: 0; }
  .divider { border: 0; border-top: 1px dashed rgba(255,255,255,0.75); margin: 8px 0 10px; }
  .testimonial cite { display: block; text-align: right; font-style: italic; margin-top: 6px; }

  .bio {
    position: absolute; top: 484px;
    font-family: "Arimo", Arial, sans-serif; font-size: 11.2px; line-height: 14.2px;
  }
  .bio-ruth { left: 36px; width: 150px; text-align: right; }
  .bio-martin { left: 368px; width: 208px; }
  .portrait { position: absolute; top: 484px; width: 80px; height: 126px; }
  .portrait-ruth { left: 192px; background: linear-gradient(180deg, #f4e6dc, var(--photo-tone)); }
  .portrait-martin { left: 282px; background: linear-gradient(180deg, #ececec, #c9c3bd); }

  /* Spine */
  .spine {
    position: absolute; left: 582px; top: 0; width: 38px; height: 756px;
    background: linear-gradient(180deg, var(--sky-light), var(--sky-deep));
  }
  .spine-text {
    position: absolute; left: 31px; top: 26px; transform-origin: 0 0; transform: rotate(90deg);
    white-space: nowrap; display: flex; align-items: center; gap: 10px; color: var(--navy);
  }
  .spine-stamp {
    font-family: "Oswald", "Arial Narrow", sans-serif; color: var(--stamp-red); font-size: 13px;
    border: 2px solid var(--stamp-red); padding: 0 4px; line-height: 1.2; letter-spacing: 0.5px;
  }
  .spine-title { font-size: 21px; font-weight: 400; }
  .spine-authors { font-size: 20px; margin-left: 60px; }
  .spine-publisher {
    position: absolute; left: 8px; top: 684px; width: 22px; height: 66px; background: var(--white);
    display: flex; align-items: center; justify-content: center;
  }
  .spine-publisher span {
    transform: rotate(90deg); white-space: nowrap; font-size: 7px; font-weight: 600; color: var(--navy);
  }

  /* Front cover */
  .front-cover {
    position: absolute; left: 620px; top: 0; width: 580px; height: 756px;
    background: linear-gradient(180deg, var(--sky-light) 0%, var(--sky-mid) 55%, var(--sky-deep) 100%);
  }
  .houses-row {
    position: absolute; left: 0; top: 0; width: 580px; height: 130px;
    background: linear-gradient(180deg, var(--white) 0%, var(--house-top) 100%);
  }
  .stamp {
    position: absolute; left: 66px; top: 112px;
    transform: rotate(-4deg); border: 7px solid var(--stamp-red);
    padding: 6px 14px 4px;
    font-family: "Oswald", "Arial Narrow", sans-serif; font-size: 56px; color: var(--stamp-red);
    letter-spacing: 1px; line-height: 1; white-space: nowrap;
  }
  .front-title {
    position: absolute; left: 0; top: 256px; width: 580px; text-align: center;
    color: var(--white); font-weight: 300; font-size: 52px; line-height: 1.1;
  }
  .front-subtitle {
    position: absolute; left: 0; top: 386px; width: 580px; text-align: center;
    color: var(--navy); font-size: 20px; line-height: 1.3; letter-spacing: 0.8px;
  }
  .house-photo {
    position: absolute; left: 0; top: 476px; width: 580px; height: 280px;
    background: linear-gradient(180deg, var(--sky-mid) 0%, var(--house-photo-wall) 45%, #cfd6dc 100%);
  }

  /* Bottom band */
  .bottom-band { position: absolute; left: 0; top: 756px; width: 1200px; height: 85px; background: var(--band-blue); }
  .front-authors {
    position: absolute; left: 620px; top: 770px; width: 580px; text-align: center;
    color: var(--white); font-size: 27px; font-weight: 400;
  }
</style>
</head>
<body>
<div class="spread">

  <section class="back-cover">
    <div class="back-copy">
      <p>Everything You Didn't Know About Property And Mortgages, But Wish You Did!</p>
      <p>Breakthrough! Mapping the Coastal Escape is the smart home buyers guide to mortgages, property, investing and making your dreams reality. This easy to read book will teach you:</p>
      <ul>
        <li>Five things you must know before buying a property and mortgage – don't approach any bank or broker before understanding this.</li>
        <li>How to maximise your chances of getting your loan approved – including help on deposit savings and working out how much you can borrow.</li>
        <li>The mortgage and property process explained in six easy steps – with the five stressful mortgage mistakes to avoid.</li>
        <li>Tips to getting smarter with your money – and how to pay off your home loan in record time.</li>
        <li>The accidental investor vs. the planned investor – and why most Australians invest for the wrong reasons.</li>
      </ul>
      <p>The Great Australian Dream of owning your own property, or starting an investment portfolio, can become a great Australian nightmare if you don't have the right knowledge and team to support you and your dreams.</p>
      <p>So before taking your next step, read this book carefully and get the insider tips to make confident decisions with your money and your future.</p>
      <hr class="divider">
      <blockquote class="testimonial">
        "Martin professionally guided me through the process of applying for my first home loan. He made what would normally be a worrying task into something enjoyable and stress-free. I found Martin's knowledge and confidence in the home loan market impressive. Thank you for helping me make my first big step into a positive future."
        <cite>Glen Tarrant, QLD</cite>
      </blockquote>
      <hr class="divider">
      <blockquote class="testimonial">
        "I can't thank you enough for looking after us for over 10 years now and 5 loans later. No such thing as too hard basket for Martin, he will find a way to get you what you need. Professional, honest and reliable, with great product knowledge – and so friendly. An asset to have on your side when investing or buying your first home!"
        <cite>Kim Ashdown, QLD</cite>
      </blockquote>
    </div>

    <p class="bio bio-ruth">Ruth Adamyan bought her first investment property in 1995 and has never looked back. As Managing Director of Harbourline Finance, she ensures all clients receive the highest level of personal service every step of the way, and enjoys helping people achieve their dream of getting into their own home or start investing. With three generations of one family as clients, Ruth is driven to share her experiences in property and mortgages – so you too can learn the easy way and avoid costly mistakes with your money.</p>
    <div class="portrait portrait-ruth" role="img" aria-label="Portrait photo of author Ruth Adamyan"></div>
    <div class="portrait portrait-martin" role="img" aria-label="Portrait photo of author Martin Kessel"></div>
    <p class="bio bio-martin">Martin Kessel is an award winning mortgage broker with Harbourline Finance. With over 40 years' experience in the finance world, he's worked in virtually every area of banking and lending in over a dozen different locations throughout Queensland. Along the way he's helped thousands of Australians secure finance for their dream home or investment property. No matter how simple or complex the challenge, with a world of insider knowledge and experience at his fingertips, you definitely want Martin to be on your finance team.</p>
  </section>

  <section class="spine">
    <div class="spine-text">
      <span class="spine-stamp">BREAKTHROUGH!</span>
      <span class="spine-title">Mapping the Coastal Escape</span>
      <span class="spine-authors">Kessel &amp; Adamyan</span>
    </div>
    <div class="spine-publisher"><span>Harbourline Finance</span></div>
  </section>

  <section class="front-cover">
    <div class="houses-row" role="img" aria-label="Row of small white model houses with one blue house among them"></div>
    <div class="stamp">BREAKTHROUGH!</div>
    <h1 class="front-title">Mapping the<br>Coastal Escape</h1>
    <p class="front-subtitle">The Smart Home Buyers Guide To<br>Mortgages, Property, Investing And<br>Making Your Dreams Reality</p>
    <div class="house-photo" role="img" aria-label="Photo of a modern white home at dusk with a green front door and lit entry path"></div>
  </section>

  <div class="bottom-band"></div>
  <p class="front-authors">Martin Kessel &amp; Ruth Adamyan</p>

</div>
</body>
</html>
```